Redesign for Real Estate Lead Generation Site

We are looking for a slight redesign for our real estate lead generation sites.

Here's one of our current sites: www.qdrhousefigures.com

The design should be simple as it is currently, remain only on one page, and nothing too detailed to where it may take a while to load/reload. We also have parallel sites, www.lmnhousefigures.com, www.lmnquicklistings.com, and a few others which all will end up utilizing the same template.

We've found that the majority of the site traffic will come from print advertising, not as much SEO. But also understand the more simple the site, the greater likelihood a user may find us through search engines. Another reason we want to keep it rather simple and clean.

The content on the page needs to remain the same, but with additional spaces for one written paragraph testimonial, and an area where we can incorporate a video. Originally, the ideal spot would be the open white space below the social media logos, but we are open to different ideas as you create the redesign.

A change in colors and simple graphics is what we're looking for most along with the testimonial / video additions. Also, we have a new logo we need incorporated into the site somewhere: http://www.brennoprintworks.com/KV-Crew-Properties.zip to download the file in different formates.

Here is our main site, www.kvcrewproperties.com through wordpress, so you can get an idea of what folks go to once they've signed up and received a confirm e-mail.

Please contact us if you have any questions. Good luck and thanks for submitting!

```html
<!DOCTYPE html>
<html lang="en">
<head>
<meta charset="utf-8">
<title>KV Crew Properties – Home Value Report</title>
<link href="https://fonts.googleapis.com/css2?family=Arimo:wght@400;700&family=Tinos&family=Oswald:wght@600&display=swap" rel="stylesheet">
<style>
:root{
  --sky-top:#2f8fd8;
  --sky-bottom:#8cc6ee;
  --form-bg:#def7c5;
  --form-band:#c6e2ad;
  --amber:#fbb71a;
  --ink:#1c1c1c;
  --muted:#555;
  --white:#ffffff;
  --video:#000000;
  --red:#b5090d;
  --btn-top:#6aa54a;
  --btn-bottom:#d4561c;
  --footer-top:#1a7fd6;
  --footer-bottom:#59b4f0;
  --grass:#6f9e3a;
  --select:#777;
}
*{box-sizing:border-box;margin:0;padding:0}
html,body{width:881px;height:1200px;overflow:hidden;background:var(--white)}
body{position:relative;font-family:"Arimo",Arial,sans-serif;color:var(--ink)}
.abs{position:absolute}

/* header */
.hero{left:0;top:0;width:881px;height:340px;background:linear-gradient(180deg,var(--sky-top),var(--sky-bottom))}
.brand{left:32px;top:30px;display:flex;align-items:center;gap:10px}
.brand-mark{width:40px;height:40px;background:var(--amber)}
.brand-name{font-size:27px;line-height:30px;color:#1f2a33;width:130px}
.hero-quote{left:638px;top:26px;width:230px;font-family:"Tinos",serif;font-size:19px;line-height:25px;color:var(--white)}
.slide{border:6px solid var(--white);box-shadow:0 4px 10px rgba(0,0,0,.35)}
.slide-photo{width:100%;height:100%;background:linear-gradient(180deg,#b8d4ee 0%,#e9e4dc 35%,#c9b7a3 60%,#4f7d33 85%,#3e6a28 100%)}
.slide-side{top:138px;width:136px;height:188px}
.slide-left{left:132px}
.slide-right{left:618px}
.slide-main{left:261px;top:83px;width:360px;height:240px;z-index:2}
.arrow{top:214px;width:26px;height:30px}

/* form */
.lead-form{left:24px;top:357px;width:833px;height:305px;background:var(--form-bg);border-radius:10px;overflow:hidden}
.form-intro{left:0;top:0;width:833px;height:66px;background:var(--form-band);padding:22px 26px 0;font-size:13.4px;line-height:17px}
.col-title{font-size:15px}
.label{font-size:10.5px;line-height:13px}
.field{background:var(--white);height:15px}
.select{background:var(--white);height:15px}
.select::after{content:"";position:absolute;right:0;top:0;width:15px;height:15px;background:var(--select)}
.select::before{content:"";position:absolute;right:4px;top:5px;border-left:4px solid transparent;border-right:4px solid transparent;border-top:5px solid var(--white);z-index:1}
.btn{border-radius:9px;background:linear-gradient(180deg,var(--btn-top),var(--btn-bottom));color:var(--white);font-size:11px;text-align:center;line-height:17px}

/* intro */
.section-bar{left:25px;top:676px;width:830px;height:40px;background:var(--amber);border-radius:8px;padding:7px 14px;font-family:"Tinos",serif;font-size:19.5px}
.intro-copy{left:40px;top:733px;width:370px;font-size:10.3px;line-height:17.2px;color:var(--muted)}
.intro-copy p{margin-bottom:17.2px}
.video{left:442px;top:734px;width:392px;height:236px;background:var(--video);border-radius:9px;color:var(--white);text-align:center}
.video-title{margin-top:67px;font-size:10.5px;font-weight:700}
.video-len{font-size:8px;color:#bbb}

/* testimonial */
.testimonial{left:7px;top:984px;width:863px;height:94px;background:var(--amber)}
.testimonial-tag{left:7px;top:980px;width:190px;height:102px;background:linear-gradient(180deg,#d0161b,var(--red));box-shadow:0 2px 6px rgba(0,0,0,.4);color:var(--white);font-family:"Oswald",sans-serif;font-size:30px;line-height:102px;text-align:center;letter-spacing:.5px}
.testimonial-tag::after{content:"";position:absolute;right:-8px;top:44px;border-top:7px solid transparent;border-bottom:7px solid transparent;border-left:8px solid var(--red)}
.testimonial-text{left:230px;top:997px;width:560px;font-size:13.6px;line-height:20.6px}
.testimonial-by{left:659px;top:1053px;font-size:13.6px}

/* footer */
.footer{left:0;top:1098px;width:881px;height:102px;background:linear-gradient(180deg,var(--footer-top),var(--footer-bottom) 85%,var(--grass) 88%,#567f2a)}
.footer-photo{left:34px;top:1110px;width:164px;height:86px;background:linear-gradient(180deg,rgba(255,255,255,0) 0%,#dfe4e8 30%,#a9b3b8 65%,#5f8b36 100%)}
.footer-info{left:250px;top:1119px;width:390px;text-align:center;color:var(--white);font-size:10.5px;line-height:15px}
.phone-pill{display:inline-block;background:#d9dde0;color:#333;border-radius:7px;padding:0 6px;font-size:9px;line-height:11px}
.follow{left:693px;top:1116px;font-family:"Tinos",serif;font-size:20px;color:#111}
.social{top:1152px;width:30px;height:30px;border-radius:4px}
</style>
</head>
<body>

<header class="abs hero">
  <div class="abs brand">
    <div class="brand-mark"></div>
    <div class="brand-name">KV Crew Properties</div>
  </div>
  <p class="abs hero-quote">"What is the current market value of my home in today's market?"</p>

  <div class="abs slide slide-side slide-left"><div class="slide-photo" role="img" aria-label="Photo of a historic white building with trees"></div></div>
  <div class="abs slide slide-side slide-right"><div class="slide-photo" role="img" aria-label="Photo of a columned building entrance"></div></div>
  <div class="abs slide slide-main"><div class="slide-photo" role="img" aria-label="Photo of a large red-roofed building behind a green lawn"></div></div>

  <svg class="abs arrow" style="left:54px" viewBox="0 0 26 30" aria-label="Previous"><path d="M18 3 L6 15 L18 27" fill="none" stroke="#fff" stroke-width="6"/></svg>
  <svg class="abs arrow" style="left:792px" viewBox="0 0 26 30" aria-label="Next"><path d="M8 3 L20 15 L8 27" fill="none" stroke="#fff" stroke-width="6"/></svg>
</header>

<section class="abs lead-form">
  <p class="abs form-intro">Fill out the form below for a FREE Comparative Market Analysis Report from KV Crew Properties for an estimate of your home's current value. The more complete the form the easier it will be to provide an accurate report regarding the value of your home.</p>

  <h2 class="abs col-title" style="left:16px;top:99px;font-weight:400">Fill out the Form</h2>
  <span class="abs label" style="left:16px;top:125px">Name</span><div class="abs field" style="left:57px;top:127px;width:194px"></div>
  <span class="abs label" style="left:16px;top:149px">Email</span><div class="abs field" style="left:57px;top:151px;width:194px"></div>
  <span class="abs label" style="left:16px;top:174px">Phone</span><div class="abs field" style="left:57px;top:176px;width:194px"></div>

  <h2 class="abs col-title" style="left:267px;top:100px;font-weight:400">Property Address</h2>
  <span class="abs label" style="left:267px;top:134px">Street Address</span><div class="abs field" style="left:341px;top:134px;width:207px"></div>
  <span class="abs label" style="left:267px;top:166px">City</span><div class="abs field" style="left:294px;top:165px;width:63px"></div>
  <span class="abs label" style="left:365px;top:166px">State</span><div class="abs select" style="left:395px;top:165px;width:48px"></div>
  <span class="abs label" style="left:453px;top:166px">Zip</span><div class="abs field" style="left:475px;top:165px;width:73px"></div>

  <h2 class="abs col-title" style="left:562px;top:101px;font-weight:400">Property Description</h2>
  <span class="abs label" style="left:562px;top:136px">Number of bedroom</span><div class="abs select" style="left:663px;top:135px;width:40px"></div>
  <span class="abs label" style="left:714px;top:136px">Bathrooms</span><div class="abs select" style="left:774px;top:135px;width:40px"></div>
  <span class="abs label" style="left:558px;top:161px">Condition</span><div class="abs select" style="left:608px;top:162px;width:206px"></div>
  <span class="abs label" style="left:564px;top:200px">Additional Comments:</span><div class="abs field" style="left:677px;top:201px;width:138px;height:60px"></div>
  <div class="abs btn" style="left:749px;top:274px;width:67px">sign up!</div>
</section>

<h2 class="abs section-bar" style="font-weight:400">Quick Intro</h2>
<div class="abs intro-copy">
  <p>Lorem ipsum dolor sit amet, consectetuer adipiscing elit, sed diam non-ummy nibh euismod tincidunt ut laoreet dolore magna aliquam erat volutpat. Ut wisi enim ad minim veniam, quis nostrud exerci tation ullamcorper sus</p>
  <p>Lorem ipsum dolor sit amet, consectetuer adipiscing elit, sed diam non-ummy nibh euismod tincidunt ut laoreet dolore magna aliquam erat volutpat. Ut wisi enim ad minim veniam, quis nostrud exerci tation ullamcorper sus</p>
  <p>Lorem ipsum dolor sit amet, consectetuer adipiscing elit, sed diam non-ummy nibh euismod tincidunt ut laoreet dolore magna aliquam erat volutpat. Ut wisi enim ad minim veniam, quis nostrud exerci tation ullamcorper sus</p>
</div>
<div class="abs btn" style="left:318px;top:926px;width:67px;font-size:9px;line-height:16px">Read more...</div>

<div class="abs video">
  <p class="video-title">Watch video</p>
  <p class="video-len">(1 minute)</p>
  <svg width="72" height="72" viewBox="0 0 72 72" style="margin-top:8px" aria-label="Play">
    <circle cx="36" cy="36" r="34" fill="#2a2a2a" stroke="#555" stroke-width="3"/>
    <path d="M27 22 L52 36 L27 50 Z" fill="#f26a1b"/>
  </svg>
</div>

<section class="abs testimonial"></section>
<div class="abs testimonial-tag">Testimonials</div>
<p class="abs testimonial-text">Lorem ipsum dolor sit amet, consectetuer adipiscing elit, sed diam nonummy nibh euismod tincidunt ut laoreet dolore magna aliquam erat volutpat. Lorem ipsum dolor sit amet, consectetuer adipiscing elit.</p>
<p class="abs testimonial-by">CEO, Brightline Webworks</p>

<footer class="abs footer"></footer>
<div class="abs footer-photo" role="img" aria-label="Photo of a grand historic building"></div>
<div class="abs footer-info">
  <p>KV Crew Properties :: Meridian 40 Homes Group :: <span class="phone-pill">877-QR-HOMES</span> ::</p>
  <p style="font-size:9.5px">info@kvcrewproperties.com</p>
  <p style="margin-top:4px">© 2010 KV Crew Properties</p>
</div>
<p class="abs follow">Follow us</p>
<div class="abs social" style="left:695px;background:#3b5b99" role="img" aria-label="Social profile"></div>
<div class="abs social" style="left:729px;background:#36b7e4" role="img" aria-label="Social profile"></div>
<div class="abs social" style="left:763px;background:#d0101c" role="img" aria-label="Social profile"></div>
<div class="abs social" style="left:797px;background:#b31217" role="img" aria-label="Video channel"></div>

</body>
</html>
```